Business Cards for company that supports physicians that do medical research

Need to create a business card for oKV Lumenta (www.okvlumenta.example), a company devoted to supporting physicians who conduct medical research. The form of the card should match the message of research and information quest. I have provided the logo of the company as an uploaded file. Designs should be simple and slick aimed at very high end clients.

Target Market(s)

Medical doctors that are also researchers

Industry/Entity Type

Medical

Contact Information for Business Card

Should feature logo and fields for personal info:
Name/title
Phone /email

Font styles to use
Serif
Sans Serif

Requirements
Must have
• oKV logo and fields for personal info:
• Name: Bartholomew Okonji
• Title: VP Research and Senior Analyst
• Phone: 418-372-9146
• email: info@okvlumenta.example
Nice to have
• Interesting cards that I've seen:
• 1- all black/charcoal or very dark background
• 2- Plastic - semi-transparent
• 3- non-standard height-width ratios
• 4- Functional cards -- USB drive incorporated
Should not have
• Too busy; needs to stay very simple

```html
<!DOCTYPE html>
<html lang="en">
<head>
<meta charset="utf-8">
<title>OKV Lumenta — Business Card</title>
<link href="https://fonts.googleapis.com/css2?family=Source+Sans+3:wght@400;600&display=swap" rel="stylesheet">
<style>
  :root {
    --backdrop: #ececec;
    --card-dark: #000000;
    --brand-green: #6cc24a;
    --brand-green-deep: #55b847;
    --brand-green-light: #7ac463;
    --brand-blue: #2b8fd6;
    --neutral-grey: #8a8a8a;
    --white: #ffffff;
  }
  * { margin: 0; padding: 0; box-sizing: border-box; }
  html, body {
    width: 1200px;
    height: 900px;
    overflow: hidden;
  }
  body {
    position: relative;
    background: var(--backdrop);
    font-family: "Source Sans 3", "Myriad Pro", sans-serif;
  }
  .card {
    position: absolute;
    top: 170px;
    width: 347px;
    height: 561px;
    overflow: hidden;
  }
  .card--front {
    left: 259px;
    background: var(--card-dark);
  }
  .card--back {
    left: 631px;
    background: linear-gradient(180deg, var(--brand-green-light) 0%, var(--brand-green-deep) 100%);
  }
  .tab {
    position: absolute;
    left: 102px;
    width: 143px;
    height: 30px;
    background: linear-gradient(180deg, var(--brand-green-light), var(--brand-green-deep));
  }
  .tab--top { top: 0; }
  .tab--bottom { bottom: 0; height: 28px; }

  .wordmark {
    position: absolute;
    left: 0;
    width: 100%;
    text-align: center;
    font-weight: 400;
    font-size: 32px;
    letter-spacing: 5px;
    text-transform: uppercase;
    line-height: 1;
  }
  .card--front .wordmark {
    top: 196px;
    color: var(--neutral-grey);
  }
  .card--back .wordmark {
    top: 384px;
    color: var(--white);
  }

  .identity {
    position: absolute;
    top: 338px;
    left: 0;
    width: 100%;
    text-align: center;
  }
  .identity__name {
    color: var(--brand-green);
    font-weight: 600;
    font-size: 18px;
    line-height: 22px;
  }
  .identity__title {
    color: var(--brand-blue);
    font-size: 15px;
    line-height: 20px;
  }
  .contact {
    position: absolute;
    top: 402px;
    left: 0;
    width: 100%;
    list-style: none;
    text-align: center;
    color: var(--brand-blue);
    font-size: 15px;
    line-height: 21px;
  }
  .contact__icon {
    display: inline-block;
    width: 11px;
    height: 11px;
    margin-right: 5px;
    vertical-align: -1px;
  }
</style>
</head>
<body>
  <section class="card card--front" aria-label="Card front">
    <div class="tab tab--top"></div>
    <div class="wordmark">oKV Lumenta</div>
    <div class="identity">
      <p class="identity__name">Bartholomew Okonji</p>
      <p class="identity__title">VP Research and Senior Analyst</p>
    </div>
    <ul class="contact">
      <li>
        <svg class="contact__icon" viewBox="0 0 12 12" aria-hidden="true">
          <path fill="#6cc24a" d="M1 4c0-2 2-3 5-3s5 1 5 3l-2 1-1-2H4L3 5zM2 6h8l1 5H1z"/>
        </svg>418-372-9146
      </li>
      <li>
        <svg class="contact__icon" viewBox="0 0 12 12" aria-hidden="true">
          <rect x="0.5" y="2.5" width="11" height="7" fill="#6cc24a"/>
          <path d="M0.5 2.5 6 7 11.5 2.5" fill="none" stroke="#000" stroke-width="1"/>
        </svg>info@okvlumenta.example
      </li>
    </ul>
    <div class="tab tab--bottom"></div>
  </section>

  <section class="card card--back" aria-label="Card back">
    <div class="wordmark">oKV Lumenta</div>
  </section>
</body>
</html>
```